Business Process / Lifecycle Diagram for Consulting Firm

We are a Delaware-based business modernization and transition-readiness firm. We need a clean, professional process diagram that visually represents our client lifecycle. This is not a marketing funnel or sales graphic — it is a product and delivery lifecycle.

The diagram must be reusable across pitch decks, one-pagers, grant applications, and our website.

Required Structure (must follow exactly)
Stage 1 — Diagnose
Enterprise Upgrade Audit (EUA)
Shift Preparedness Gauge™ (SPG)
(Parallel entry points, equal visual weight)

→ Output: Diagnostic Insight & Priority Signals

Stage 2 — Clarify
Modernization Roadmap (Co-Created)

Stage 3 — Modernize
Q7 — Margin & Momentum Track

Stage 4 — Sustain
Ongoing Modernization Support

Foundation Layer (supports all stages)
HRG-OS™ pillars: People, Process, Systems, Insight

End Outcome
- Operational Clarity
- Sustainable Profitability
- Long-Term Stability

Design Requirements
- Professional, calm (not startup / SaaS style)
- Minimal text, clear hierarchy
- Horizontal or left-to-right flow preferred
- No funnels, no sales language, no aggressive arrows
- Must be delivered as editable vector (AI, SVG, or Figma)

Brand Notes
- Neutral color palette that complements logo attached (Gold Color Code C39E11, Navy Blue code 002C55)
- One accent color for emphasis
- Clean typography
- Should feel credible to business owners, advisors, and lenders
- See website (https://www.hazelmereridgegroup.com/) and LinkedIn (https://www.hazelmereridgegroup.com/) for additional insight into branding.

What NOT to Do
- Do not rename stages
- Do not combine stages
- Do not add extra steps

```html
<!DOCTYPE html>
<html lang="en">
<head>
<meta charset="utf-8">
<title>Hazelmere Ridge Group — Client Lifecycle Diagram Options</title>
<link href="https://fonts.googleapis.com/css2?family=Lato:wght@400;700;900&display=swap" rel="stylesheet">
<style>
  :root {
    --navy: #002c55;
    --gold: #c39e11;
    --ink: #1f2a36;
    --muted: #5b6470;
    --rule: #b9bec6;
    --board: #e9eaec;
    --paper: #ffffff;
    --sky: #8fd0f0;
  }
  html, body {
    margin: 0;
    width: 1200px;
    height: 286px;
    overflow: hidden;
    background: var(--board);
  }
  .board { display: block; width: 1200px; height: 286px; }
  text { font-family: "Lato", sans-serif; }
  .sheet { fill: var(--paper); }
  .brand-name { fill: var(--navy); font-size: 21px; font-weight: 700; letter-spacing: .5px; }
  .bar-label { fill: #fff; font-size: 13px; font-weight: 900; }
  .badge { fill: #fff; stroke-width: 2.5; }
  .badge-num { font-size: 12px; font-weight: 700; text-anchor: middle; }
  .item { fill: var(--muted); font-size: 10px; }
  .chev { fill: none; stroke: #a0a6ae; stroke-width: 1.3; }
  .divider { stroke: var(--rule); stroke-width: 1; stroke-dasharray: 3 3; fill: none; }
  .pill { fill: var(--gold); }
  .pill-text { fill: #fff; font-size: 9px; font-weight: 700; text-anchor: middle; }
  .panel { fill: var(--navy); }
  .panel-title { fill: #fff; font-size: 14px; font-weight: 900; text-anchor: middle; }
  .panel-item { fill: #fff; font-size: 12.5px; }
  .panel-chev { fill: none; stroke: #fff; stroke-width: 1.5; }
  .foundation-title { fill: var(--ink); font-size: 14px; text-anchor: middle; }
  .foundation-sub { fill: var(--muted); font-size: 12px; text-anchor: middle; }
  .navy-fill { fill: var(--navy); }
  .gold-fill { fill: var(--gold); }
  .stage-tag { fill: #fff; font-size: 11px; font-weight: 700; text-anchor: middle; }
  .stage-name { fill: var(--navy); font-size: 13px; font-weight: 700; }
  .small { fill: var(--muted); font-size: 7.5px; }
  .small-gold { fill: var(--gold); font-size: 8px; text-decoration: underline; }
  .out-item { fill: #fff; font-size: 8px; }
  .out-title { fill: #fff; font-size: 11px; font-weight: 700; text-anchor: middle; }
  .icon-line { fill: none; stroke: #fff; stroke-width: 2.4; stroke-linecap: round; }
  .icon-navy { fill: none; stroke: var(--navy); stroke-width: 2.4; stroke-linecap: round; }
  .path-navy { fill: none; stroke: var(--navy); stroke-width: 13; stroke-linejoin: round; }
  .path-gold { fill: none; stroke: var(--gold); stroke-width: 13; stroke-linejoin: round; }
  .ring-navy { fill: #fff; stroke: var(--navy); stroke-width: 9; }
  .ring-gold { fill: #fff; stroke: var(--gold); stroke-width: 9; }
  .ring-num { fill: var(--ink); font-size: 15px; font-weight: 700; text-anchor: middle; }
  .step-title { fill: var(--ink); font-size: 13px; font-weight: 700; text-anchor: middle; }
  .step-text { fill: #3d4652; font-size: 11.5px; text-anchor: middle; }
  .step-output { fill: var(--gold); font-size: 13px; font-weight: 700; text-anchor: middle; }
  .stem-navy { stroke: var(--navy); stroke-width: 3; }
  .stem-gold { stroke: var(--gold); stroke-width: 3; }
  .arrow-down { fill: none; stroke: var(--ink); stroke-width: 1.4; }
</style>
</head>
<body>
<svg class="board" viewBox="0 0 2576 614" xmlns="http://www.w3.org/2000/svg" aria-label="Three layout options for the Hazelmere Ridge Group client lifecycle diagram">
  <defs>
    <linearGradient id="plinth-navy" x1="0" y1="0" x2="0" y2="1">
      <stop offset="0" stop-color="#c9d3de"/>
      <stop offset=".35" stop-color="#5a7392"/>
      <stop offset="1" stop-color="#002c55"/>
    </linearGradient>
    <linearGradient id="plinth-gold" x1="0" y1="0" x2="0" y2="1">
      <stop offset="0" stop-color="#efe3b6"/>
      <stop offset=".35" stop-color="#d8ba4c"/>
      <stop offset="1" stop-color="#c39e11"/>
    </linearGradient>
    <filter id="lift" x="-5%" y="-5%" width="110%" height="115%">
      <feDropShadow dx="0" dy="2" stdDeviation="3" flood-color="#000" flood-opacity=".12"/>
    </filter>
  </defs>

  <!-- ===== Option A: horizontal bar ===== -->
  <g class="option option-bar">
    <rect class="sheet" x="16" y="18" width="990" height="534" filter="url(#lift)"/>
    <text class="brand-name" x="42" y="90">HAZELMERE RIDGE GROUP</text>

    <g class="stage-bar">
      <rect class="navy-fill" x="41" y="133" width="174" height="27"/>
      <rect class="gold-fill" x="215" y="133" width="163" height="27"/>
      <rect class="navy-fill" x="378" y="133" width="187" height="27"/>
      <rect class="gold-fill" x="565" y="133" width="192" height="27"/>
      <text class="bar-label" x="58" y="151">DIAGNOSE</text>
      <text class="bar-label" x="230" y="151">CLARIFY</text>
      <text class="bar-label" x="396" y="151">MODERNIZE</text>
      <text class="bar-label" x="584" y="151">SUSTAIN</text>
      <circle class="badge" cx="203" cy="146" r="13" stroke="#002c55"/>
      <text class="badge-num" x="203" y="151" fill="#002c55">01</text>
      <circle class="badge" cx="364" cy="146" r="13" stroke="#c39e11"/>
      <text class="badge-num" x="364" y="151" fill="#c39e11">02</text>
      <circle class="badge" cx="555" cy="146" r="13" stroke="#002c55"/>
      <text class="badge-num" x="555" y="151" fill="#002c55">03</text>
      <circle class="badge" cx="741" cy="146" r="13" stroke="#c39e11"/>
      <text class="badge-num" x="741" y="151" fill="#c39e11">04</text>
    </g>

    <g class="column-dividers">
      <line class="divider" x1="204" y1="162" x2="204" y2="455"/>
      <line class="divider" x1="365" y1="162" x2="365" y2="455"/>
      <line class="divider" x1="556" y1="162" x2="556" y2="455"/>
    </g>

    <g class="stage-items">
      <path class="chev" d="M42 177l5 5-5 5M47 177l5 5-5 5"/>
      <text class="item" x="63" y="186">Enterprise Upgrade Audit</text>
      <text class="item" x="63" y="201">(EUA)</text>
      <path class="chev" d="M42 215l5 5-5 5M47 215l5 5-5 5"/>
      <text class="item" x="63" y="224">Shift Preparedness Gauge™</text>
      <text class="item" x="63" y="239">(SPG)</text>
      <path class="arrow-down" d="M72 249v12M68 257l4 4 4-4"/>
      <rect class="pill" x="42" y="268" width="59" height="20" rx="10"/>
      <text class="pill-text" x="71.5" y="281">OUTPUT</text>
      <text class="item" x="43" y="306" style="font-size:9.5px">Diagnostic Insight &amp; Priority Signals</text>

      <path class="chev" d="M224 177l5 5-5 5M229 177l5 5-5 5"/>
      <text class="item" x="241" y="185">Modernization Roadmap</text>
      <text class="item" x="241" y="201">(Co-Created)</text>

      <path class="chev" d="M394 177l5 5-5 5M399 177l5 5-5 5"/>
      <text class="item" x="415" y="186">Q7 — Margin &amp; Momentum</text>
      <text class="item" x="415" y="202">Track</text>

      <path class="chev" d="M582 177l5 5-5 5M587 177l5 5-5 5"/>
      <text class="item" x="603" y="186">Ongoing Modernization</text>
      <text class="item" x="603" y="202">Support</text>
    </g>

    <g class="stage-visuals">
      <rect x="42" y="320" width="116" height="100" rx="22" fill="url(#plinth-navy)" role="img" aria-label="Navy pedestal with a diagnostic magnifier icon"/>
      <rect x="228" y="300" width="116" height="122" rx="22" fill="url(#plinth-gold)" role="img" aria-label="Gold pedestal with two people planning at a board"/>
      <rect x="395" y="306" width="116" height="114" rx="22" fill="url(#plinth-navy)" role="img" aria-label="Navy pedestal with a laptop and gear systems icon"/>
      <rect x="605" y="306" width="116" height="114" rx="22" fill="url(#plinth-gold)" role="img" aria-label="Gold pedestal with a globe and leaves sustainability icon"/>
    </g>

    <path class="divider" d="M98 422v40h566v-40"/>

    <g class="outcome-panel">
      <rect class="panel" x="779" y="131" width="210" height="289" rx="14"/>
      <text class="panel-title" x="871" y="191">OUTPUT</text>
      <path class="panel-chev" d="M807 213l5 5-5 5M813 213l5 5-5 5"/>
      <text class="panel-item" x="831" y="223">Operational Clarity</text>
      <path class="panel-chev" d="M807 248l5 5-5 5M813 248l5 5-5 5"/>
      <text class="panel-item" x="831" y="258">Sustainable Profitability</text>
      <path class="panel-chev" d="M807 282l5 5-5 5M813 282l5 5-5 5"/>
      <text class="panel-item" x="834" y="292">Long-Term Stability</text>
      <g class="growth-icon" fill="none" stroke="#8fd0f0" stroke-width="3.5" stroke-linecap="round">
        <path d="M872 354l-20-20M852 334v10M852 334h10"/>
        <path d="M887 350v-24M880 332l7-7 7 7"/>
        <path d="M902 354l20-20M922 334v10M922 334h-10"/>
      </g>
      <circle cx="887" cy="380" r="14" fill="#5b3b8c"/>
      <circle cx="887" cy="380" r="5" fill="#fff"/>
    </g>

    <text class="foundation-title" x="420" y="494">Foundation Layer</text>
    <text class="foundation-sub" x="435" y="520">HRG-OS™ pillars: People, Process, Systems, Insight</text>
  </g>

  <!-- ===== Option B: ribbon ===== -->
  <g class="option option-ribbon">
    <rect class="sheet" x="1032" y="20" width="734" height="412" filter="url(#lift)"/>
    <text class="brand-name" x="1410" y="94" text-anchor="middle">HAZELMERE RIDGE GROUP</text>

    <g class="ribbon-bands">
      <polygon class="gold-fill" points="1155,205 1208,148 1208,205 1155,262"/>
      <polygon class="gold-fill" points="1290,205 1345,148 1345,205 1290,258"/>
      <polygon class="gold-fill" points="1428,205 1482,148 1482,205 1428,258"/>
      <polygon class="gold-fill" points="1565,200 1617,148 1617,205 1565,255"/>
    </g>

    <g class="ribbon-stages">
      <polygon class="navy-fill" points="1075,125 1155,122 1155,262 1115,252 1075,262"/>
      <polygon class="navy-fill" points="1208,138 1290,138 1290,255 1249,245 1208,255"/>
      <polygon class="navy-fill" points="1345,137 1428,138 1428,255 1387,245 1345,255"/>
      <polygon class="navy-fill" points="1482,137 1565,138 1565,255 1523,245 1482,255"/>

      <circle class="gold-fill" cx="1114" cy="177" r="24"/>
      <circle class="icon-line" cx="1111" cy="174" r="9"/>
      <path class="icon-line" d="M1118 181l8 8"/>
      <circle class="gold-fill" cx="1249" cy="174" r="24"/>
      <path class="icon-line" d="M1240 165h18v12h-18zM1244 186v-6M1254 186v-6"/>
      <circle class="gold-fill" cx="1387" cy="174" r="24"/>
      <circle class="icon-line" cx="1387" cy="174" r="8"/>
      <path class="icon-line" d="M1387 162v-3M1387 189v-3M1375 174h-3M1402 174h-3"/>
      <circle class="gold-fill" cx="1523" cy="174" r="24"/>
      <circle class="icon-line" cx="1523" cy="174" r="10"/>
      <path class="icon-line" d="M1513 174h20M1523 164c-5 6-5 14 0 20"/>

      <text class="stage-tag" x="1114" y="226">STAGE 1</text>
      <text class="stage-tag" x="1249" y="222">STAGE 2</text>
      <text class="stage-tag" x="1387" y="222">STAGE 3</text>
      <text class="stage-tag" x="1523" y="222">STAGE 4</text>
    </g>

    <g class="ribbon-outcome">
      <polygon class="navy-fill" points="1617,138 1722,138 1722,322 1724,322 1656,420 1588,322 1617,322"/>
      <text class="out-title" x="1656" y="184">OUTCOMES</text>
      <text class="out-item" x="1633" y="209">Operational</text>
      <text class="out-item" x="1633" y="223">Clarity</text>
      <text class="out-item" x="1634" y="244">Sustainable</text>
      <text class="out-item" x="1633" y="258">Profitability</text>
      <text class="out-item" x="1633" y="280">Long-Term</text>
      <text class="out-item" x="1633" y="294">Stability</text>
    </g>

    <g class="ribbon-labels">
      <text class="stage-name" x="1075" y="282">Diagnose</text>
      <circle cx="1078" cy="296" r="2" fill="#a0a6ae"/>
      <text class="small" x="1085" y="299">Enterprise Upgrade Audit</text>
      <text class="small" x="1085" y="313">(EUA)</text>
      <circle cx="1078" cy="324" r="2" fill="#a0a6ae"/>
      <text class="small" x="1085" y="327">Shift Preparedness Gauge™</text>
      <text class="small" x="1085" y="341">(SPG)</text>
      <path class="arrow-down" d="M1090 348v10M1087 355l3 3 3-3"/>
      <text class="small-gold" x="1075" y="370">Output:</text>
      <circle cx="1078" cy="382" r="2" fill="#a0a6ae"/>
      <text class="small" x="1085" y="385">Diagnostic Insight &amp; Priority Signals</text>

      <text class="stage-name" x="1210" y="278">Clarify</text>
      <circle cx="1214" cy="293" r="2" fill="#a0a6ae"/>
      <text class="small" x="1222" y="296">Modernization Roadmap</text>
      <text class="small" x="1222" y="308">(Co-Created)</text>

      <text class="stage-name" x="1347" y="278">Modernize</text>
      <circle cx="1352" cy="293" r="2" fill="#a0a6ae"/>
      <text class="small" x="1360" y="296">Q7 — Margin &amp; Momentum</text>
      <text class="small" x="1360" y="308">Track</text>

      <text class="stage-name" x="1486" y="278">Sustain</text>
      <circle cx="1489" cy="293" r="2" fill="#a0a6ae"/>
      <text class="small" x="1496" y="296">Ongoing Modernization</text>
      <text class="small" x="1496" y="308">Support</text>
    </g>

    <path class="divider" d="M1076 392v15h431v-90"/>
    <text class="small" x="1187" y="423">Foundation Layer</text>
    <text class="small" x="1263" y="423">HRG-OS™ pillars: People, Process, Systems, Insight</text>
  </g>

  <!-- ===== Option C: rising path ===== -->
  <g class="option option-path">
    <rect class="sheet" x="1786" y="20" width="734" height="560" filter="url(#lift)"/>
    <text class="brand-name" x="1830" y="100">HAZELMERE RIDGE GROUP</text>

    <g class="rising-path">
      <polyline class="path-navy" points="1883,377 1915,346 2005,340 2020,340"/>
      <polyline class="path-gold" points="2020,340 2052,305 2135,303 2149,302"/>
      <polyline class="path-navy" points="2149,302 2185,268 2265,268 2280,271"/>
      <polyline class="path-gold" points="2280,271 2320,236 2400,234 2415,234"/>
      <polyline class="path-navy" points="2415,234 2448,202 2520,200"/>
    </g>

    <g class="stems">
      <line class="stem-navy" x1="1883" y1="325" x2="1883" y2="370"/>
      <line class="stem-navy" x1="2019" y1="284" x2="2019" y2="334"/>
      <line class="stem-gold" x1="2147" y1="248" x2="2147" y2="296"/>
      <line class="stem-navy" x1="2278" y1="216" x2="2278" y2="265"/>
      <line class="stem-gold" x1="2413" y1="180" x2="2413" y2="228"/>
    </g>

    <g class="nodes">
      <circle class="navy-fill" cx="1883" cy="377" r="12"/>
      <circle cx="2020" cy="340" r="12" fill="#c39e11" stroke="#fff" stroke-width="3"/>
      <circle class="navy-fill" cx="2149" cy="302" r="12"/>
      <circle cx="2280" cy="271" r="12" fill="#c39e11" stroke="#fff" stroke-width="3"/>
      <circle class="navy-fill" cx="2415" cy="234" r="12"/>
    </g>

    <g class="stage-rings">
      <text class="step-title" x="1880" y="221">Diagnose</text>
      <circle class="ring-navy" cx="1883" cy="285" r="40"/>
      <text class="ring-num" x="1882" y="271">01</text>
      <circle class="icon-navy" cx="1880" cy="288" r="9"/>
      <path class="icon-navy" d="M1887 295l7 7"/>

      <text class="step-title" x="2010" y="186">Clarify</text>
      <circle class="ring-gold" cx="2018" cy="246" r="38"/>
      <text class="ring-num" x="2018" y="234">02</text>
      <path class="icon-navy" d="M2010 246h16v10h-16z" style="stroke:#c39e11"/>

      <text class="step-title" x="2142" y="152">Modernize</text>
      <circle cx="2147" cy="210" r="38" fill="#fff" stroke="#002c55" stroke-width="9"/>
      <text class="ring-num" x="2147" y="197">03</text>
      <circle class="icon-navy" cx="2147" cy="216" r="7"/>

      <text class="step-title" x="2274" y="128">Sustain</text>
      <circle class="ring-gold" cx="2278" cy="178" r="38"/>
      <text class="ring-num" x="2278" y="165">04</text>
      <circle cx="2278" cy="184" r="9" fill="none" stroke="#c39e11" stroke-width="2.4"/>

      <circle cx="2413" cy="142" r="42" fill="none" stroke="#002c55" stroke-width="3"/>
      <circle class="navy-fill" cx="2413" cy="142" r="36"/>
      <text x="2413" y="146" fill="#fff" font-size="8.5" font-weight="700" text-anchor="middle">OUTCOMES</text>
    </g>

    <g class="step-details">
      <text class="step-text" x="1885" y="408">Enterprise Upgrade Audit</text>
      <text class="step-text" x="1885" y="424">(EUA)</text>
      <text class="step-text" x="1885" y="441">Shift Preparedness</text>
      <text class="step-text" x="1885" y="457">Gauge™ (SPG)</text>
      <path class="arrow-down" d="M1880 466v13M1876 475l4 4 4-4"/>
      <text class="step-output" x="1876" y="501">Output</text>
      <text class="step-text" x="1882" y="516">Diagnostic Insight &amp;</text>
      <text class="step-text" x="1882" y="531">Priority Signals</text>

      <text class="step-text" x="2020" y="377">Modernization</text>
      <text class="step-text" x="2020" y="393">Roadmap</text>
      <text class="step-text" x="2020" y="410">(Co-Created)</text>

      <text class="step-text" x="2152" y="357">Q7 — Margin &amp;</text>
      <text class="step-text" x="2152" y="376">Momentum Track</text>

      <text class="step-text" x="2280" y="319">Ongoing</text>
      <text class="step-text" x="2280" y="338">Modernization</text>
      <text class="step-text" x="2280" y="357">Support</text>

      <text class="step-text" x="2430" y="277">Operational Clarity</text>
      <text class="step-text" x="2430" y="296">Sustainable Profitability</text>
      <text class="step-text" x="2430" y="316">Long-Term Stability</text>
    </g>

    <path class="divider" d="M1874 540v20h573v-238"/>
    <text class="foundation-title" x="2133" y="521">Foundation Layer</text>
    <text class="foundation-sub" x="2152" y="540" style="font-size:11px">HRG-OS™ pillars: People, Process, Systems, Insight</text>
  </g>
</svg>
</body>
</html>
```